Makeup brushes and lashes brochure for vibrant new brand!

(UPDATE we have added a sample brochure for your guidance. Similar layout required,brush description is not necessary in lengthy form,brush number and title is acceptable))We are looking for an enthusiastic designer to work with us on our new 3fold brochure of our products. The brochure will be included in customers orders to entice them to make more purchases. All products must be displayed in along witglh the product name/ numbers.

We have three product ranges,makeup brushes,false lashes and cosmetic sponge. The brochure should tie in with our other packaging themes and be clear and modern.

The following information is required:

Company description-
Established in 2015 by Professional Makeup Artist Maura Delaney, Dab&Glow is one of Irelands leading cosmetic brands. We provide the beauty industry with incredibly high quality makeup brushes and Luxury Lashes.
Expertly design by Maura and handmade using incredibly high quality natural and synthetic hair.

Brush Care-(To be placed after brush imagery and descriptions.)

Keep'em clean! To keep your brushes in their best shape possible,clean them once a week with warm soapy water. Avoid submerging the ferrule Metal part) in water as this could loosen the glue inside and cause the hair to shed. Shedding is normal for the first few washes.
Rinse the brush well with clean water and air dry flat.

Lash Care-( To be placed after lash imagery and descriptions.)

All our lashes are re-usable so take care of them and you will have fluttery long lashes for up to 30 wears!

We recommend cleaning your lashes after every 3 wears.

Firstly, remove any left over glue from the lash band and soak the lashes in warm soapy water for 5 minutes. Remove and rinse and residue from the lash. re-Shape and Replace the lash back into its case and let dry naturally. As good as new!

Brushes descriptions- (Please crop brush images to below logo on handle.)

BRUSH SETS

Quite Rosy Glow - Containing 8 professional brushes,this set is your go to for your everyday makeup application. DG01,DG02 , DG03,DG04,DG05,DG06,DG10,DG24

Top Lids Set- Contain 8 of our incredible eye brushes for expert application. DG02,DG06,DG12,DG14,DG16,DG18,DG20,DG24

Sharp Cheek set- The ideal mix containing 6 of our most popular face and eye brushes. DG07,DG09,DG14,DG16,DG18,DG24.

INDIVIDUAL BRUSHES

DG01- Large synthetic powder brush. Ideal for use with powder foundations,creams or liquids.

DG02- Ideal for detailed eye work, Using ultra soft hair ,it won't irritate the delicate eye area.

DG03- Domed Shape,synthetic hair, the DG03 is perfect for seamlessly buffing liquid,creams,gel based foundations into the skin for a flawless finish.

DG04- Ultra soft synthetic hair,DG04 is a must have multi task brush. From concealer to eyeshadow application this all rounder is essential in the makeup bag.

DG05- Silky soft blush brush applies the perfect amount of product for flawless skin.

DG06- Precisely blends shadows into the socket of the eye for controlled blending.

DG08- NEW!(BOLD Writing) Domed shadow blending brush,ideal for softening edges.

DG09- The unique tapered shape on our contour is perfect for chiseling out cheekbones or simply adding a pop of colour to the cheeks using the flat sides. (Synthetic)

DG10- Synthetic hair,DG10 is ultra thin with a precise angle ,ideal for creating winged eyeliner or definition to brows.

DG12- Our finest blending brush yet! This truly is a must have for anyone who loves to add precise detail to their makeup looks. Super soft and light, it blends with ease for a flawless finish.

DG14- This is the ultimate brush for under eye blending! Dense, silky and sturdy, it is simply an essential in any eye look.

DG16- Another must have for any makeup bag is our flat shading brush. No more fall out from eyeshadows as this controls the placement perfectly.( Synthetic)

DG18- If your looking to pack on colour to a specific area or to smudge out for a smokey effect this nifty little brush is one for the collection.(Synthetic)

DG20- An all rounder brush, our flat definer is a real multitasker. From defining the brows to cutting the crease there is no job too big or too small for the DG20. (Synthetic)

DG24- Ultra soft and dense. Hand crafted ,tapered hair blends shadows effortlessly.

LASHES
3 lash ranges-
VelTrim-
Luxury meets glamour. Each lash is designed to give your peepers that beautiful full lash look with added volume and glamour. Made from silk fibres and a flexible cotton band,you'll love the comfort!

Aurora -
Our lightest lash range yet! Made from ethically soured human hair,each lash oozes femininity and natural volume. You wont feel like your wearing lashes at all!

DewPoint Sponge-

Our innovative design makes blending creams or liquids a dream! Just dampen your sponge and apply your product to the skin. We recommend using the round side in bouncing motions to blend foundation and the flat side to push the product into the skin. The pointed end is specifically designed to get into those hard to reach areas,under eye area,around the nose etc.

Sponge cleaning instructions-( To be placed after lash imagery and descriptions.)

We recommend replacing your sponge every 6weeks. To clean your DewPoint Sponge,soak the sponge in hot soapy water and rinse until all makeup has been removed. Squeeze out excess water and allow to dry flat in a well ventilated room.

Information for end of brochure-
Visit www.dabandglow.example for prices and more information on all products.

Social media icons-
Facebook
Instagram
twitter

Choice of several brand logo jpeg and png.
Any further questions,we are happy to answer them.

Target Market(s)

Young,women

Industry/Entity Type

Hair And Beauty

Font styles to use
Other font styles liked:
• GeoSans Light

Colors
ecdaeb
eea4c8
e667a6
e34298
a64599
b868aa
000000
ffffff

Requirements
Must have
• Vibrant colour,sleek flow throughout brochure.
Should not have
• Images of people.

```html
<!DOCTYPE html>
<html lang="en">
<head>
<meta charset="utf-8">
<title>Dab&amp;Glow – Inner Brochure</title>
<link rel="stylesheet" href="https://fonts.googleapis.com/css2?family=Dosis:wght@400;500;600;700&display=swap">
<style>
  :root {
    --pink: #e34298;
    --pink-hot: #e667a6;
    --pink-soft: #eea4c8;
    --pink-pale: #ecdaeb;
    --ink: #151417;
    --ink-2: #1f1d22;
    --white: #ffffff;
    --black: #000000;
    --font: "Dosis", sans-serif;
  }
  * { box-sizing: border-box; margin: 0; padding: 0; }
  html, body { width: 1200px; height: 1006px; overflow: hidden; background: #f2f2f2; }
  body { font-family: var(--font); color: var(--white); }

  .brochure { display: flex; width: 1200px; height: 1006px; }
  .panel { position: relative; width: 400px; height: 1006px; overflow: hidden; }
  .panel--dark { background: linear-gradient(160deg, var(--ink-2), var(--ink) 60%, #0e0d10); }
  .panel--pink { background: linear-gradient(90deg, var(--pink) 0%, var(--pink-hot) 50%, var(--pink) 100%); }
  .swoosh { position: absolute; left: 0; width: 400px; pointer-events: none; }
  .swoosh--top { top: 0; height: 140px; }
  .swoosh--bottom { bottom: 0; height: 120px; }
  .panel__body { position: relative; z-index: 1; }

  .pill {
    display: inline-block; background: var(--white); color: var(--black);
    border-radius: 10px; font-weight: 500; font-size: 22px; letter-spacing: .5px;
    padding: 4px 16px; line-height: 1.2;
  }

  /* Brush item */
  .brush { display: flex; flex-direction: column; align-items: center; width: 72px; }
  .brush__photo {
    width: 54px; height: 54px; border-radius: 50%; border: 3px solid var(--pink);
    background: radial-gradient(circle at 50% 50%, #ffffff 0%, #f1eef0 55%, #d9d3d7 100%);
    box-shadow: 0 0 0 1px rgba(255,255,255,.4);
  }
  .brush__photo--empty { background: var(--white); }
  .brush__code { font-size: 10px; font-weight: 700; margin-top: 5px; letter-spacing: .3px; }

  /* Sets panel */
  .sets { padding-top: 82px; text-align: center; }
  .set { margin-bottom: 14px; }
  .set__title {
    display: inline-block; font-size: 16px; font-weight: 500; letter-spacing: .4px;
    border-bottom: 1.5px solid var(--white); padding: 0 6px 2px; margin-bottom: 6px;
  }
  .set__desc { font-size: 13px; line-height: 1.35; padding: 0 22px; margin-bottom: 8px; }
  .set__row { display: flex; justify-content: center; gap: 4px; margin-bottom: 6px; }
  .set__row--spread { justify-content: space-between; padding: 0 12px; }
  .web { position: absolute; z-index: 2; bottom: 20px; font-size: 13px; font-weight: 600; color: var(--white); }
  .web--left { left: 20px; }
  .web--right { right: 20px; }

  /* Individual panel */
  .individual { padding-top: 26px; text-align: center; }
  .individual__grid { display: grid; grid-template-columns: 1fr 1fr; column-gap: 18px; padding: 18px 14px 0; }
  .item { display: flex; flex-direction: column; align-items: center; height: 158px; }
  .item__desc { font-size: 10px; line-height: 1.35; min-height: 52px; margin-bottom: 8px; }
  .item .brush__photo { border-color: var(--black); border-width: 2px; width: 56px; height: 56px; }
  .footer-web { position: absolute; bottom: 22px; left: 0; right: 0; display: flex; align-items: center; justify-content: center; gap: 8px; font-size: 13px; font-weight: 600; }
  .footer-web::before, .footer-web::after { content: ""; width: 86px; height: 1px; background: var(--white); }

  /* Right panel */
  .more { padding-top: 108px; }
  .more__grid { display: grid; grid-template-columns: 1fr 1fr; column-gap: 16px; padding: 0 14px; }
  .more .item { height: 172px; }
  .more .item__desc { min-height: 60px; }
  .more .item--solo { grid-column: 1 / span 2; height: 130px; }
  .more .item--solo .item__desc { min-height: 32px; }
  .more .brush__photo { border-color: var(--pink); border-width: 3px; }
  .care { text-align: center; margin-top: 24px; }
  .care__text { text-align: justify; font-size: 12.5px; line-height: 1.35; padding: 12px 18px 0; }
  .care__text p + p { margin-top: 12px; }
  .brand { position: absolute; z-index: 2; left: 40px; bottom: 60px; font-size: 28px; font-weight: 500; color: var(--white); display: flex; align-items: center; gap: 8px; }
  .brand__dot { width: 12px; height: 12px; border-radius: 50%; background: var(--pink); }
</style>
</head>
<body>
<main class="brochure">

  <!-- Panel 1: brush sets -->
  <section class="panel panel--dark">
    <svg class="swoosh swoosh--top" viewBox="0 0 400 140" preserveAspectRatio="none" aria-hidden="true">
      <path d="M0 0 H400 V92 C330 40 180 30 0 48 Z" fill="var(--pink)"/>
      <path d="M0 56 C180 38 330 48 400 100" fill="none" stroke="var(--black)" stroke-width="4"/>
      <path d="M0 64 C180 48 330 58 400 110" fill="none" stroke="var(--black)" stroke-width="2"/>
    </svg>
    <svg class="swoosh swoosh--bottom" viewBox="0 0 400 120" preserveAspectRatio="none" aria-hidden="true">
      <path d="M0 20 C140 30 300 70 400 14 V120 H0 Z" fill="var(--pink)"/>
      <path d="M0 10 C140 20 300 58 400 4" fill="none" stroke="var(--black)" stroke-width="4"/>
      <path d="M0 30 C140 40 300 80 400 26" fill="none" stroke="var(--ink)" stroke-width="2"/>
    </svg>
    <div class="panel__body sets">
      <span class="pill">BRUSH SETS</span>

      <div class="set" style="margin-top:16px">
        <h2 class="set__title">QUITE ROSY GLOW</h2>
        <p class="set__desc">Containing 8 professional brushes,this set is your go to for your everyday makeup application</p>
        <div class="set__row">
          <div class="brush"><div class="brush__photo" role="img" aria-label="DG01 brush photo"></div><span class="brush__code">DG01</span></div>
          <div class="brush"><div class="brush__photo" role="img" aria-label="DG02 brush photo"></div><span class="brush__code">DG02</span></div>
          <div class="brush"><div class="brush__photo" role="img" aria-label="DG03 brush photo"></div><span class="brush__code">DG03</span></div>
          <div class="brush"><div class="brush__photo" role="img" aria-label="DG04 brush photo"></div><span class="brush__code">DG04</span></div>
          <div class="brush"><div class="brush__photo" role="img" aria-label="DG05 brush photo"></div><span class="brush__code">DG05</span></div>
        </div>
        <div class="set__row">
          <div class="brush"><div class="brush__photo" role="img" aria-label="DG06 brush photo"></div><span class="brush__code">DG06</span></div>
          <div class="brush"><div class="brush__photo" role="img" aria-label="DG10 brush photo"></div><span class="brush__code">DG10</span></div>
          <div class="brush"><div class="brush__photo" role="img" aria-label="DG24 brush photo"></div><span class="brush__code">DG24</span></div>
        </div>
      </div>

      <div class="set" style="margin-top:20px">
        <h2 class="set__title">TOP LIDS SET</h2>
        <p class="set__desc">Contain 8 of our incredible eye brushes for expert application</p>
        <div class="set__row">
          <div class="brush"><div class="brush__photo" role="img" aria-label="DG02 brush photo"></div><span class="brush__code">DG02</span></div>
          <div class="brush"><div class="brush__photo" role="img" aria-label="DG06 brush photo"></div><span class="brush__code">DG06</span></div>
          <div class="brush"><div class="brush__photo" role="img" aria-label="DG12 brush photo"></div><span class="brush__code">DG12</span></div>
          <div class="brush"><div class="brush__photo" role="img" aria-label="DG14 brush photo"></div><span class="brush__code">DG14</span></div>
          <div class="brush"><div class="brush__photo" role="img" aria-label="DG16 brush photo"></div><span class="brush__code">DG16</span></div>
        </div>
        <div class="set__row">
          <div class="brush"><div class="brush__photo" role="img" aria-label="DG18 brush photo"></div><span class="brush__code">DG18</span></div>
          <div class="brush"><div class="brush__photo" role="img" aria-label="DG20 brush photo"></div><span class="brush__code">DG20</span></div>
          <div class="brush"><div class="brush__photo" role="img" aria-label="DG24 brush photo"></div><span class="brush__code">DG24</span></div>
        </div>
      </div>

      <div class="set" style="margin-top:20px">
        <h2 class="set__title">SHARP CHEEK SET</h2>
        <p class="set__desc">The ideal mix containing 6 of our most popular face and eye brushes</p>
        <div class="set__row set__row--spread">
          <div class="brush"><div class="brush__photo brush__photo--empty" role="img" aria-label="DG07 brush photo"></div><span class="brush__code">DG07</span></div>
          <div class="brush"><div class="brush__photo" role="img" aria-label="DG09 brush photo"></div><span class="brush__code">DG09</span></div>
          <div class="brush"><div class="brush__photo" role="img" aria-label="DG14 brush photo"></div><span class="brush__code">DG14</span></div>
          <div class="brush"><div class="brush__photo" role="img" aria-label="DG16 brush photo"></div><span class="brush__code">DG16</span></div>
        </div>
        <div class="set__row" style="gap:30px">
          <div class="brush"><div class="brush__photo" role="img" aria-label="DG18 brush photo"></div><span class="brush__code">DG18</span></div>
          <div class="brush"><div class="brush__photo" role="img" aria-label="DG24 brush photo"></div><span class="brush__code">DG24</span></div>
        </div>
      </div>
    </div>
    <span class="web web--left">www.dabandglow.example</span>
  </section>

  <!-- Panel 2: individual brushes -->
  <section class="panel panel--pink">
    <div class="panel__body individual">
      <span class="pill">INDIVIDUAL BRUSHES</span>
      <div class="individual__grid">
        <div class="item"><p class="item__desc">Large synthetic powder brush. Ideal for use with powder foundations,creams or liquids</p><div class="brush__photo" role="img" aria-label="DG01 brush photo"></div><span class="brush__code">DG01</span></div>
        <div class="item"><p class="item__desc">Ideal for detailed eye work, Using ultra soft hair ,it won't irritate the delicate eye area.</p><div class="brush__photo" role="img" aria-label="DG02 brush photo"></div><span class="brush__code">DG02</span></div>
        <div class="item"><p class="item__desc">Domed Shape,synthetic hair, the DG03 is perfect for seamlessly buffing liquid,creams,gel based foundations into the skin for a flawless finish</p><div class="brush__photo" role="img" aria-label="DG03 brush photo"></div><span class="brush__code">DG03</span></div>
        <div class="item"><p class="item__desc">Ultra soft synthetic hair,DG04 is a must have multi task brush. From concealer to eyeshadow application this all rounder is essential in the makeup bag</p><div class="brush__photo" role="img" aria-label="DG04 brush photo"></div><span class="brush__code">DG04</span></div>
        <div class="item"><p class="item__desc">Silky soft blush brush applies the perfect amount of product for flawless skin</p><div class="brush__photo" role="img" aria-label="DG05 brush photo"></div><span class="brush__code">DG05</span></div>
        <div class="item"><p class="item__desc">Precisely blends shadows into the socket of the eye for controlled blending</p><div class="brush__photo" role="img" aria-label="DG06 brush photo"></div><span class="brush__code">DG06</span></div>
        <div class="item"><p class="item__desc">NEW!(BOLD Writing) Domed shadow blending brush,ideal for softening edges</p><div class="brush__photo" role="img" aria-label="DG08 brush photo"></div><span class="brush__code">DG08</span></div>
        <div class="item"><p class="item__desc">The unique tapered shape on our contour is perfect for chiseling out cheekbones or simply adding a pop of colour to the cheeks using the flat sides. (Synthetic)</p><div class="brush__photo" role="img" aria-label="DG09 brush photo"></div><span class="brush__code">DG09</span></div>
        <div class="item"><p class="item__desc">Synthetic hair,DG10 is ultra thin with a precise angle ,ideal for creating winged eyeliner or definition to brows</p><div class="brush__photo" role="img" aria-label="DG10 brush photo"></div><span class="brush__code">DG10</span></div>
        <div class="item"><p class="item__desc">Our finest blending brush yet! This truly is a must have for anyone who loves to add precise detail to their makeup looks. Super soft and light, it blends with ease for a flawless finish</p><div class="brush__photo" role="img" aria-label="DG12 brush photo"></div><span class="brush__code">DG12</span></div>
      </div>
    </div>
    <div class="footer-web">www.dabandglow.example</div>
  </section>

  <!-- Panel 3: more brushes and care -->
  <section class="panel panel--dark">
    <svg class="swoosh swoosh--top" viewBox="0 0 400 140" preserveAspectRatio="none" aria-hidden="true">
      <path d="M0 0 H400 V90 C300 70 120 50 0 84 Z" fill="var(--pink)"/>
      <path d="M0 92 C120 56 300 78 400 98" fill="none" stroke="var(--black)" stroke-width="4"/>
      <path d="M0 102 C120 66 300 88 400 108" fill="none" stroke="var(--black)" stroke-width="2"/>
    </svg>
    <svg class="swoosh swoosh--bottom" viewBox="0 0 400 120" preserveAspectRatio="none" aria-hidden="true">
      <path d="M0 70 C120 20 300 10 400 22 V120 H0 Z" fill="var(--pink)"/>
      <path d="M0 60 C120 10 300 0 400 12" fill="none" stroke="var(--black)" stroke-width="4"/>
      <path d="M0 80 C120 32 300 22 400 34" fill="none" stroke="var(--ink)" stroke-width="2"/>
    </svg>
    <div class="panel__body more">
      <div class="more__grid">
        <div class="item"><p class="item__desc">This is the ultimate brush for under eye blending! Dense, silky and sturdy, it is simply an essential in any eye look.</p><div class="brush__photo" role="img" aria-label="DG14 brush photo"></div><span class="brush__code">DG14</span></div>
        <div class="item"><p class="item__desc">Another must have for any makeup bag is our flat shading brush. No more fall out from eyeshadows as this controls the placement perfectly.( Synthetic)</p><div class="brush__photo" role="img" aria-label="DG16 brush photo"></div><span class="brush__code">DG16</span></div>
        <div class="item"><p class="item__desc">If your looking to pack on colour to a specific area or to smudge out for a smokey effect this nifty little brush is one for the collection.(Synthetic)</p><div class="brush__photo" role="img" aria-label="DG18 brush photo"></div><span class="brush__code">DG18</span></div>
        <div class="item"><p class="item__desc">An all rounder brush, our flat definer is a real multitasker. From defining the brows to cutting the crease there is no job too big or too small for the DG20. (Synthetic)</p><div class="brush__photo" role="img" aria-label="DG20 brush photo"></div><span class="brush__code">DG20</span></div>
        <div class="item item--solo"><p class="item__desc">Ultra soft and dense. Hand crafted ,<br>tapered hair blends shadows effortlessly</p><div class="brush__photo" role="img" aria-label="DG24 brush photo"></div><span class="brush__code">DG24</span></div>
      </div>
      <div class="care">
        <span class="pill">BRUSH CARE</span>
        <div class="care__text">
          <p>Keep'em clean! To keep your brushes in their best shape possible,clean them once a week with warm soapy water. Avoid submerging the ferrule Metal part) in water as this could loosen the glue inside and cause the hair to shed. Shedding is normal for the first few washes.</p>
          <p>Rinse the brush well with clean water and air dry flat.</p>
        </div>
      </div>
    </div>
    <div class="brand"><span class="brand__dot"></span>Dab&amp;Glow</div>
    <span class="web web--right">www.dabandglow.example</span>
  </section>

</main>
</body>
</html>
```